An KADORI MIRETSU certified teacher needs a Business Card Design.

I need a business card to introduce and promote myself as an KADORI MIRETSU certified teacher and florist for fresh floral decoration services of venues ranging from executive rooms to large business and social events. I would prefer sober card with coloured avatar or vector image of a simple KADORI MIRETSU arrangement that has clear floral impression on the business card with my face book, and website address and other contact details like skype, cell and landlines, etc.
I have Teachers Fourth Grade Diploma, and Teaching Membership of Miretsu Mentors Guild (MMG), Japan.

Target Market(s)

Hospitality industry (Hotels, Cafes, Residency), Business organisations (executive rooms, meeting areas, conferences), Individuals & families (parties, social events), Hospitals and Clinics, etc.

Industry/Entity Type

Teacher

Contact Information for Business Card

Nazneen Bilqees
Certified Teacher, Miretsu Academy of Kadori
Cell: +92 317 604 5192
email: petalworx.pk@bloomvia.example
Facebook: http://www.facebook-sample.example/petalworx.pk
Website: www.petalworx.example

Requirements
Nice to have
• Avatar or vector of a classic/basic KADORI MIRETSU arrangement with vivid colour flowers
Should not have
• images of living things like women, etc.

```html
<!DOCTYPE html>
<html lang="en">
<head>
<meta charset="utf-8">
<title>Nazneen Bilqees – Business Card</title>
<link href="https://fonts.googleapis.com/css2?family=Oswald:wght@400&family=Ubuntu:wght@300;400&display=swap" rel="stylesheet">
<style>
  :root {
    --page: #ffffff;
    --card: #ffffff;
    --frame: #b8385a;
    --name: #7b8a3c;
    --role: #b3224f;
    --school: #f2cdd5;
    --contact: #5b3a2c;
    --seal: #c9453a;
    --faint-mark: #f1ebdc;
    --art-a: #f6e9e3;
    --art-b: #d8a0a6;
  }
  * { box-sizing: border-box; margin: 0; padding: 0; }
  html, body { width: 1200px; height: 648px; overflow: hidden; background: var(--page); }
  .sheet { position: relative; width: 1200px; height: 648px; }

  .card {
    position: absolute; top: 135px; width: 512px; height: 291px;
    background: var(--card); border: 2px solid var(--frame);
    font-family: "Ubuntu", sans-serif; overflow: hidden;
  }
  .card--front { left: 50px; }
  .card--alt { left: 633px; }

  .arrangement { position: absolute; left: 6px; top: 6px; width: 190px; height: 280px; }

  .faint-mark {
    position: absolute; left: 112px; top: 212px;
    font-family: "Ubuntu", sans-serif; font-weight: 400; font-size: 26px;
    color: var(--faint-mark); letter-spacing: 1px;
  }

  .badge {
    position: absolute; left: 10px; top: 12px;
    display: flex; align-items: center; gap: 4px;
    font-family: "Ubuntu", sans-serif; font-weight: 400; font-size: 11px;
    color: var(--contact); letter-spacing: .5px;
  }
  .badge__square { width: 14px; height: 14px; border: 1.5px solid var(--contact); }
  .card--alt .badge { flex-direction: column; align-items: flex-start; gap: 2px; top: 20px; left: 22px; color: var(--seal); font-size: 9px; }
  .card--alt .badge__square { width: 26px; height: 26px; border-color: var(--seal); }

  .name {
    position: absolute; left: 210px; top: -4px;
    font-family: "Oswald", sans-serif; font-weight: 400; font-size: 41px;
    color: var(--name); text-transform: uppercase; letter-spacing: .3px; white-space: nowrap;
  }
  .role {
    position: absolute; font-family: "Ubuntu", sans-serif; font-weight: 300;
    font-size: 35px; color: var(--role); line-height: 1;
  }
  .role--florist { left: 253px; top: 64px; }
  .role--teacher { left: 361px; top: 86px; }
  .school {
    position: absolute; left: 273px; top: 104px;
    font-family: "Ubuntu", sans-serif; font-weight: 400; font-size: 20px;
    color: var(--school); text-transform: uppercase; letter-spacing: .3px;
  }

  .contact {
    position: absolute; left: 229px; top: 167px;
    list-style: none; color: var(--contact);
    font-size: 17.5px; line-height: 28.5px; font-weight: 400; white-space: nowrap;
  }
</style>
</head>
<body>
<main class="sheet">

  <article class="card card--front">
    <svg class="arrangement" viewBox="0 0 190 280" role="img" aria-label="Illustration of a Kadori Miretsu floral arrangement: plum blossom branch, pink flowers and a black ring vessel">
      <defs>
        <radialGradient id="art-front" cx="55%" cy="55%" r="60%">
          <stop offset="0" stop-color="var(--art-b)"/>
          <stop offset=".55" stop-color="var(--art-a)"/>
          <stop offset="1" stop-color="var(--card)"/>
        </radialGradient>
      </defs>
      <rect width="190" height="280" fill="url(#art-front)"/>
    </svg>
    <span class="faint-mark">MIRETSU</span>
    <div class="badge"><span class="badge__square"></span><span>KADORI GLOBAL</span></div>

    <h1 class="name">Nazneen Bilqees</h1>
    <span class="role role--florist">florist</span>
    <span class="school">Miretsu</span>
    <span class="role role--teacher">teacher</span>

    <ul class="contact">
      <li>Cell: +92 317 604 5192</li>
      <li>www.petalworx.example</li>
      <li>fb-sample.example/petalworx</li>
      <li>petalworx.pk@bloomvia.example</li>
    </ul>
  </article>

  <article class="card card--alt">
    <svg class="arrangement" viewBox="0 0 190 280" role="img" aria-label="Illustration of a Kadori Miretsu floral arrangement: plum blossom branch, pink flowers and a black ring vessel">
      <defs>
        <radialGradient id="art-alt" cx="55%" cy="55%" r="60%">
          <stop offset="0" stop-color="var(--art-b)"/>
          <stop offset=".55" stop-color="var(--art-a)"/>
          <stop offset="1" stop-color="var(--card)"/>
        </radialGradient>
      </defs>
      <rect width="190" height="280" fill="url(#art-alt)"/>
    </svg>
    <span class="faint-mark">MIRETSU</span>
    <div class="badge"><span class="badge__square"></span><span>KADORI GLOBAL</span></div>

    <h1 class="name">Nazneen Bilqees</h1>
    <span class="role role--florist">florist</span>
    <span class="school">Miretsu</span>
    <span class="role role--teacher">teacher</span>

    <ul class="contact">
      <li>Cell: +92 317 604 5192</li>
      <li>www.petalworx.example</li>
      <li>fb-sample.example/petalworx</li>
      <li>petalworx.pk@bloomvia.example</li>
    </ul>
  </article>

</main>
</body>
</html>
```